Machine shop looking for a Brochure about us

We are Tarvel Tooling a growing machine shop in CT that is in need of a Brochure about us.

the Brochure will be a single flip book (4 pages in total)

The first page will be just our logo and our slogan with few machined parts. Something like the picture that is attached to this.

The second page will be about the company and our quality policy.

The third page will be about the machines we have and our capacity.

And the back side I would like to keep simple maybe the logo in the back again with few good words. any suggestions would be preferred .
Updates

Hello all designers and the Flyers are looking really good! few quick things. we are a machine shop that make parts for all different kinds of industries and just not airplane companies so a generic milling machine or generic machined parts work better for pictures on the flyers. Also, I am not sure how some designers are using Tarvel Tooling instead of Tarvel tooling for information. Anyhow they are looking really good and we will be picking the designer this Tuesday.

Target Market(s)

venders and customers

Industry/Entity Type

Shop

Font styles to use
Sans Serif

Colors
0255a3
fbed22

Requirements
Must have
• must use our logo colors
• state that we are as9100 certified and also iso 9001
• please email me for more information and questions. I attached a business plan that you can work from.

```html
<!DOCTYPE html>
<html lang="en">
<head>
<meta charset="utf-8">
<title>Tarvel Tooling – About Us</title>
<link href="https://fonts.googleapis.com/css2?family=Exo+2:wght@300;400;600;700&display=swap" rel="stylesheet">
<style>
  :root{
    --navy-top:#262955;
    --navy-bottom:#2f3990;
    --navy-ink:#2a2f6e;
    --gold:#fdd000;
    --white:#ffffff;
  }
  html,body{margin:0;padding:0;overflow:hidden;}
  body{width:849px;height:1200px;}
  .page{
    position:relative;width:849px;height:1200px;overflow:hidden;
    background:linear-gradient(180deg,var(--navy-top) 0%,var(--navy-bottom) 100%);
    font-family:"Exo 2",sans-serif;color:var(--white);
  }
  .headline{
    position:absolute;right:507px;top:170px;margin:0;
    text-align:right;font-size:39px;line-height:39px;font-weight:300;
    text-transform:uppercase;letter-spacing:.2px;
  }
  .headline strong{color:var(--gold);font-weight:700;}
  .tool-visual{
    position:absolute;left:92px;top:326px;width:240px;height:874px;
    background:var(--gold);
  }
  .about{position:absolute;left:400px;top:166px;width:362px;}
  .section-title{
    margin:0 0 8px;color:var(--gold);font-size:16px;font-weight:600;
    text-transform:uppercase;letter-spacing:-.1px;line-height:20px;
  }
  .about p{
    margin:0 0 8px;font-size:14.6px;line-height:23.4px;font-weight:400;
    hyphens:auto;-webkit-hyphens:auto;
  }
  .about .section-title.policy{margin-top:16px;margin-bottom:2px;}
  .features{position:absolute;left:400px;top:721px;width:400px;}
  .feature{display:flex;align-items:flex-start;height:117.6px;}
  .feature-icon{flex:0 0 78px;width:78px;height:78px;}
  .feature-text{margin-left:18px;padding-top:4px;}
  .feature-title{margin:0;color:var(--gold);font-size:12.4px;font-weight:700;text-transform:uppercase;line-height:15.6px;}
  .feature-body{margin:0;font-size:11.2px;line-height:15.6px;text-transform:uppercase;font-weight:400;}
</style>
</head>
<body>
<main class="page">
  <h1 class="headline"><strong>An enduring<br>reputation</strong> for<br>quality tooling</h1>

  <div class="tool-visual" role="img" aria-label="Illustration of a yellow spiral end mill cutting tool"></div>

  <section class="about">
    <h2 class="section-title">A team with decades of experience</h2>
    <p>Tarvel Tooling is a fully equipped machine shop that has employed 4-7 people over the last three years. It is experienced in machining steel, stainless steel, aluminum, nickel and titanium. It has four CNC lathes, three 3 axis milling machines and a 4 axis milling machine. It also has a full deburring area, tool room and an inspection area including CMM capabilities.</p>
    <p>Tarvel Tooling is currently located at 482 Alder Road in Brookfield, CT. The company moved in to this location 2 years ago. At that time the building infrastructure was completely refurbished and tailored a machine shop environment.</p>
    <h2 class="section-title policy">Quality policy</h2>
    <p>Tarvel Tooling is AS9100 and ISO 9001 certified, with a combined 36 years of experience in the manufacturing industry, and understands the importance of meeting commitments and your needs. Tarvel Tooling has an excellent reputation in the industry for its product quality.</p>
  </section>

  <section class="features">
    <div class="feature">
      <svg class="feature-icon" viewBox="0 0 78 78" aria-hidden="true">
        <circle cx="39" cy="39" r="39" fill="var(--gold)"/>
        <g fill="none" stroke="var(--navy-ink)" stroke-width="3" stroke-linecap="round" stroke-linejoin="round">
          <path d="M29 22l3 3 5-6M29 33l3 3 5-6"/>
          <path d="M42 23h10M42 34h10"/>
        </g>
        <path d="M18 50h10c4 0 6 3 10 3h8l10-8c2-1 4 1 3 3l-9 9H30l-8 3z" fill="var(--navy-ink)"/>
      </svg>
      <div class="feature-text">
        <h3 class="feature-title">Quality assurance system</h3>
        <p class="feature-body">Ur suntione dunt ipsuntist aut rest<br>quia alignim coria volorendaes ut quos<br>aspicia qui tem do</p>
      </div>
    </div>
    <div class="feature">
      <svg class="feature-icon" viewBox="0 0 78 78" aria-hidden="true">
        <circle cx="39" cy="39" r="39" fill="var(--gold)"/>
        <g fill="none" stroke="var(--navy-ink)" stroke-width="3" stroke-linecap="round">
          <circle cx="44" cy="42" r="15"/>
          <path d="M44 22v5M40 20h8M44 42l-4 4M56 28l3-3"/>
          <path d="M16 38h10M14 44h10M18 50h10"/>
        </g>
      </svg>
      <div class="feature-text">
        <h3 class="feature-title">Mission-critical turnaround</h3>
        <p class="feature-body">Ur suntione dunt ipsuntist aut rest<br>quia alignim coria volorendaes ut quos<br>aspicia qui tem do</p>
      </div>
    </div>
    <div class="feature">
      <svg class="feature-icon" viewBox="0 0 78 78" aria-hidden="true">
        <circle cx="39" cy="39" r="39" fill="var(--gold)"/>
        <g fill="none" stroke="var(--navy-ink)" stroke-width="3" stroke-linejoin="round">
          <path d="M28 25h22l7 9-18 22-18-22z"/>
          <path d="M21 34h36M33 25l-3 9 9 22 9-22-3-9"/>
        </g>
      </svg>
      <div class="feature-text">
        <h3 class="feature-title">Committment to satisfaction</h3>
        <p class="feature-body">Ur suntione dunt ipsuntist aut rest<br>quia alignim coria volorendaes ut quos<br>aspicia qui tem do</p>
      </div>
    </div>
  </section>
</main>
</body>
</html>
```